Banner ad design for Vantora Display Ads

We are looking for a designer to develop a concept for banner ads for a Vantora Display campaign we are building.

We have 3 business lines, shredding services, records management services and scanning services.

We are looking for 4 sets of ads to be created, one for each business line + one set that showcases all of our lines together.

For the design concepts, we would like to see a few sizes (banner, square, leaderboard, skyscraper, etc) for each.

The person chosen will then need to create the ads into all Vantora supported sizes -- 20 sizes total for each set of ads as per the Vantora size guidelines found on this page - https://help.vantora-example.com/vantora-ads/answer/4827150?hl=en&ref_topic=6604821#

A few items to note:
- Design should complement our existing brand/website look and feel (www.oak-ferry.ca)
- Each final ad must be 150Kb or less in size
- Final designs should be editable, meaning if we would like to change some copy in the design, we can do so using a well-known software (Canva, Photoshop/InDesign, etc)
- Some images are attached for use, but if you feel a different stock image is more suitable to to your design, please go ahead and use it.

Provided below is some messaging that can be used for each set of ads. Do not feel you need to use all of the messaging, it is provided for guidance.

SHREDDING SERVICES:

Possible Short Headline:
-- One-Time Shredding Services
-- Secure Shredding Services
-- Affordable On-Site Shredding

Possible Long Headline
-- Your Paper Can be Destroyed as Soon as the Next Business Day

Possible Descriptions:
-- KVEC Gold Certified On site shredding company. Service as soon as Next Day.
-- Secure and Affordable Toronto & GTA On-Site Shredding.
-- Certified, Affordable Office Shredding Since 2003.
-- Quick, no contact and affordable paper shredding services in Toronto & Southern Ontario.
-- Certified, Affordable Office Shredding Since 2003. Fast, no contact shredding service.

Call to Action
-- Get a Quote

RECORDS MANAGEMENT
Short Headline:
-- Off-site Records Storage
-- Records Management & Storage
-- Secure Records Storage
-- Records Management Services
-- Long Term Records Management
-- Document Storage Solutions

Possible Description
-- Local, Affordable Storage Solutions. Protect and Store your Documents in our Secure Facility
-- Local, Affordable Records Management Solutions. Store your Records in our Secure Facility
-- Certified, Affordable Document Storage Since 2004. Contact Us for a Free Quote!
-- Vaultline+ Certified, Affordable Document Storage Since 2004. Contact Us for a Free Quote!

Call to Action
-- Get a Quote

SCANNING SERVICES

Short Headline:
-- Professional Scanning Company
-- Toronto & GTA Scanning Service
-- Document Scanning Services
-- Digital Conversion Services
-- Fast & Easy Retrieval

Description
-- Scan and documents and files with Professional scanning services from Oak-Ferry
-- Convert Your Paper Files to Electronic Files. Fast & Easy Retrieval.
-- Easily access your documents electronically with Document Scanning Services

Call to Action
-- Get a Quote

ALL SERVICES AD SET
Short Headline
-- Shred, Scan & Store Documents
-- Secure Shredding, Records Management and Scanning Services
-- #1 Document Management Company
-- Oak Ferry Shredding, Storage & Scanning

Description
-- Secure and Affordable Toronto & GTA On-Site Shredding, Document Storage & Scanning Company

Call to Action
-- Get a Quote

Font styles to use
Sans Serif

```html
<!DOCTYPE html>
<html lang="en">
<head>
<meta charset="utf-8">
<title>Vantora Display Ads – Document Storage Solutions</title>
<link rel="stylesheet" href="https://fonts.googleapis.com/css2?family=Montserrat:wght@500;600;700;800&display=swap">
<style>
  :root {
    --canvas: #e6e6e6;
    --brand-blue: #2170a9;
    --cta-orange: #f9a11b;
    --white: #ffffff;
    --ink: #1d5f92;
    --muted: #4a4a4a;
    --photo-a: #c9b08a;
    --photo-b: #3b5f9c;
    --photo-c: #e9e3d6;
  }
  * { margin: 0; padding: 0; box-sizing: border-box; }
  html, body { width: 1200px; height: 1133px; overflow: hidden; background: var(--canvas); }
  body { position: relative; font-family: "Montserrat", Arial, sans-serif; }

  .ad { position: absolute; overflow: hidden; background: var(--white); }
  .ad-shapes { position: absolute; inset: 0; width: 100%; height: 100%; display: block; }
  .fill-blue { fill: var(--brand-blue); }
  .fill-white { fill: var(--white); }
  .fill-photo { fill: url(#warehouse-tones); }

  .headline { position: absolute; color: var(--white); font-weight: 800; letter-spacing: 0.2px; }
  .description { position: absolute; color: var(--white); font-weight: 500; }

  .cta {
    position: absolute; background: var(--cta-orange); color: var(--white);
    font-weight: 600; display: flex; align-items: center; justify-content: center;
    border-radius: 2px;
  }

  .brand { position: absolute; display: flex; flex-direction: column; }
  .brand-name { display: flex; align-items: center; gap: 5px; color: var(--ink); font-weight: 700; line-height: 1; }
  .brand-mark { background: var(--ink); display: inline-block; }
  .brand-tagline { color: var(--muted); font-weight: 500; line-height: 1.2; margin-top: 3px; }

  /* Leaderboard */
  .ad-leaderboard { left: 128px; top: 90px; width: 1000px; height: 125px; }
  .ad-leaderboard .headline { right: 22px; top: 12px; font-size: 27px; text-align: right; }
  .ad-leaderboard .description { right: 22px; top: 58px; font-size: 13.5px; line-height: 21px; text-align: right; }
  .ad-leaderboard .cta { left: 394px; top: 63px; width: 213px; height: 48px; font-size: 17px; }
  .ad-leaderboard .brand { left: 7px; top: 90px; }
  .ad-leaderboard .brand-name { font-size: 13px; }
  .ad-leaderboard .brand-mark { width: 8px; height: 8px; }
  .ad-leaderboard .brand-tagline { font-size: 7px; }

  /* Medium square */
  .ad-square-sm { left: 126px; top: 256px; width: 413px; height: 344px; }
  .ad-square-sm .headline { left: 26px; top: 16px; font-size: 28px; line-height: 35px; }
  .ad-square-sm .description { left: 26px; top: 133px; font-size: 12.5px; line-height: 19.5px; }
  .ad-square-sm .cta { left: 220px; top: 285px; width: 171px; height: 47px; font-size: 15px; }
  .ad-square-sm .brand { left: 20px; top: 283px; }
  .ad-square-sm .brand-name { font-size: 17px; }
  .ad-square-sm .brand-mark { width: 10px; height: 10px; }
  .ad-square-sm .brand-tagline { font-size: 8.5px; }

  /* Large square */
  .ad-square-lg { left: 126px; top: 697px; width: 463px; height: 387px; }
  .ad-square-lg .headline { left: 26px; top: 22px; font-size: 29px; line-height: 35px; }
  .ad-square-lg .description { left: 26px; top: 142px; font-size: 12.5px; line-height: 19.5px; }
  .ad-square-lg .cta { left: 232px; top: 319px; width: 192px; height: 54px; font-size: 17px; }
  .ad-square-lg .brand { left: 25px; top: 312px; }
  .ad-square-lg .brand-name { font-size: 19px; }
  .ad-square-lg .brand-mark { width: 11px; height: 11px; }
  .ad-square-lg .brand-tagline { font-size: 9.5px; }

  /* Skyscraper */
  .ad-skyscraper { left: 713px; top: 256px; width: 412px; height: 827px; }
  .ad-skyscraper .headline { left: 0; right: 0; top: 36px; font-size: 31px; line-height: 41px; text-align: center; }
  .ad-skyscraper .description { left: 0; right: 0; top: 132px; font-size: 16px; line-height: 27px; text-align: center; }
  .ad-skyscraper .cta { left: 190px; top: 743px; width: 192px; height: 55px; font-size: 17px; }
  .ad-skyscraper .brand { left: 21px; top: 741px; }
  .ad-skyscraper .brand-name { font-size: 19px; }
  .ad-skyscraper .brand-mark { width: 11px; height: 11px; }
  .ad-skyscraper .brand-tagline { font-size: 9.5px; }
</style>
</head>
<body>

<svg width="0" height="0" style="position:absolute" aria-hidden="true">
  <defs>
    <linearGradient id="warehouse-tones" x1="0" y1="0" x2="1" y2="1">
      <stop offset="0" stop-color="#7b8aa6"/>
      <stop offset="0.35" stop-color="#c9b08a"/>
      <stop offset="0.6" stop-color="#3b5f9c"/>
      <stop offset="0.85" stop-color="#e2d8c6"/>
      <stop offset="1" stop-color="#b99e77"/>
    </linearGradient>
  </defs>
</svg>

<!-- Leaderboard -->
<section class="ad ad-leaderboard">
  <svg class="ad-shapes" viewBox="0 0 1000 125" preserveAspectRatio="none">
    <polygon class="fill-photo" points="0,0 400,0 545,125 0,125" role="img" aria-label="Photo of tall blue warehouse shelving stacked with archive boxes"/>
    <polygon class="fill-white" points="382,0 1000,0 1000,125 526,125"/>
    <polygon class="fill-blue" points="392,0 1000,0 1000,125 538,125"/>
    <polygon class="fill-white" points="0,30 190,125 0,125"/>
  </svg>
  <h1 class="headline">Document Storage Solutions</h1>
  <p class="description">Local, Affordable Storage Solutions. Protect and<br>Store your Documents in our Secure Facility</p>
  <div class="cta">Get a Quote</div>
  <div class="brand">
    <span class="brand-name"><span class="brand-mark"></span>oak-ferry</span>
    <span class="brand-tagline">Information Security</span>
  </div>
</section>

<!-- Medium square -->
<section class="ad ad-square-sm">
  <svg class="ad-shapes" viewBox="0 0 413 344" preserveAspectRatio="none">
    <rect class="fill-photo" x="0" y="0" width="413" height="344" role="img" aria-label="Photo of tall blue warehouse shelving stacked with archive boxes"/>
    <polygon class="fill-white" points="0,0 316,0 162,262 0,241"/>
    <polygon class="fill-blue" points="0,0 306,0 152,260 0,241"/>
    <polygon class="fill-white" points="0,241 413,283 413,344 0,344"/>
  </svg>
  <h2 class="headline">Document<br>Storage<br>Solutions</h2>
  <p class="description">Local, Affordable Storage<br>Solutions. Protect and<br>Store your Documents in<br>our Secure Facility</p>
  <div class="brand">
    <span class="brand-name"><span class="brand-mark"></span>oak-ferry</span>
    <span class="brand-tagline">Information Security</span>
  </div>
  <div class="cta">Get a Quote</div>
</section>

<!-- Large square -->
<section class="ad ad-square-lg">
  <svg class="ad-shapes" viewBox="0 0 463 387" preserveAspectRatio="none">
    <rect class="fill-photo" x="0" y="0" width="463" height="387" role="img" aria-label="Photo of tall blue warehouse shelving stacked with archive boxes"/>
    <polygon class="fill-white" points="0,0 317,0 154,286 0,267"/>
    <polygon class="fill-blue" points="0,0 306,0 143,284 0,267"/>
    <polygon class="fill-white" points="0,267 463,330 463,387 0,387"/>
  </svg>
  <h2 class="headline">Document<br>Storage<br>Solutions</h2>
  <p class="description">Local, Affordable Storage<br>Solutions. Protect and<br>Store your Documents in<br>our Secure Facility</p>
  <div class="brand">
    <span class="brand-name"><span class="brand-mark"></span>oak-ferry</span>
    <span class="brand-tagline">Information Security</span>
  </div>
  <div class="cta">Get a Quote</div>
</section>

<!-- Skyscraper -->
<section class="ad ad-skyscraper">
  <svg class="ad-shapes" viewBox="0 0 412 827" preserveAspectRatio="none">
    <polygon class="fill-blue" points="0,0 412,0 412,293 0,241"/>
    <polygon class="fill-blue" points="0,666 412,610 412,745"/>
    <polygon class="fill-photo" points="0,267 412,304 412,610 0,666" role="img" aria-label="Photo of tall blue warehouse shelving stacked with archive boxes"/>
    <polygon class="fill-white" points="0,666 412,745 412,827 0,827"/>
  </svg>
  <h2 class="headline">Document Storage<br>Solutions</h2>
  <p class="description">Local, Affordable Storage<br>Solutions. Protect and Store your<br>Documents in our Secure Facility</p>
  <div class="brand">
    <span class="brand-name"><span class="brand-mark"></span>oak-ferry</span>
    <span class="brand-tagline">Information Security</span>
  </div>
  <div class="cta">Get a Quote</div>
</section>

</body>
</html>
```